Meridian Lodging Partners

An Editable Business Card Template For MLP & MLH
Similar or Different Design

418 W. Harlan Brookside Pkwy.
Suite 2270
Irving, TX 75091

```html
<!DOCTYPE html>
<html lang="en">
<head>
<meta charset="utf-8">
<title>Meridian Lodging Partners – Business Card</title>
<link href="https://fonts.googleapis.com/css2?family=Arimo:wght@400;700&display=swap" rel="stylesheet">
<style>
  :root {
    --brand-red: #8b1a1d;
    --brand-red-light: #931f23;
    --card-white: #f7f7f7;
    --ink: #3a3a3a;
    --ink-soft: #5b5b5b;
    --backdrop: #e6e6e6;
    --white: #ffffff;
  }
  * { margin: 0; padding: 0; box-sizing: border-box; }
  html, body { width: 1200px; height: 1200px; overflow: hidden; }
  body {
    background: var(--backdrop);
    font-family: "Arimo", Arial, sans-serif;
    position: relative;
  }
  .card {
    position: absolute;
    left: 262px;
    width: 686px;
    height: 392px;
    border-radius: 22px;
    overflow: hidden;
  }
  .card--front { top: 165px; background: var(--card-white); }
  .card--back {
    top: 653px;
    background: linear-gradient(180deg, var(--brand-red-light), var(--brand-red));
    color: var(--white);
  }

  /* Brand mark: plain circle with name */
  .brand-seal {
    position: absolute;
    width: 198px;
    height: 198px;
    border-radius: 50%;
    display: flex;
    align-items: center;
    justify-content: center;
    text-align: center;
    font-weight: 700;
    font-size: 21px;
    line-height: 1.25;
  }
  .card--front .brand-seal { left: 71px; top: 83px; background: var(--brand-red); color: var(--white); }
  .card--back .brand-seal { left: 367px; top: 110px; background: var(--white); color: var(--brand-red); }

  /* Front contact block */
  .contact { position: absolute; left: 395px; top: 90px; color: var(--ink); }
  .contact__name { font-size: 22px; font-weight: 700; color: var(--brand-red); line-height: 26px; }
  .contact__title { font-size: 15px; color: var(--ink-soft); line-height: 18px; }
  .contact__address { margin-top: 17px; font-size: 15px; line-height: 19px; }
  .contact__list { list-style: none; margin-top: 14px; font-size: 15px; line-height: 19.5px; }
  .contact__list li { display: flex; align-items: center; gap: 9px; }
  .contact__list svg { width: 14px; height: 14px; fill: var(--brand-red); flex: none; }

  .tagline-band {
    position: absolute;
    left: 0; right: 0; top: 327px;
    height: 29px;
    background: var(--brand-red);
    color: var(--white);
    font-weight: 700;
    font-size: 20px;
    line-height: 29px;
    text-align: center;
  }

  /* Back */
  .pitch { position: absolute; left: 50px; top: 78px; }
  .pitch__heading { font-size: 19px; font-weight: 700; line-height: 24px; }
  .benefits { list-style: none; margin-top: 20px; }
  .benefits li {
    display: flex; align-items: center; gap: 10px;
    font-size: 15.5px; height: 38.7px;
  }
  .benefits svg { width: 20px; height: 20px; flex: none; }
</style>
</head>
<body>

<section class="card card--front">
  <div class="brand-seal">Meridian<br>Lodging<br>Partners</div>

  <div class="contact">
    <div class="contact__name">Dana Whitcombe</div>
    <div class="contact__title">Sales Manager</div>
    <div class="contact__address">418 W. Harlan Brookside Pkwy.<br>Suite 2270, Irving, TX 75091</div>
    <ul class="contact__list">
      <li><svg viewBox="0 0 24 24"><path d="M6.6 10.8a15.1 15.1 0 0 0 6.6 6.6l2.2-2.2c.3-.3.7-.4 1-.2 1.1.4 2.3.6 3.6.6.6 0 1 .4 1 1V20c0 .6-.4 1-1 1A17 17 0 0 1 3 4c0-.6.4-1 1-1h3.5c.6 0 1 .4 1 1 0 1.3.2 2.5.6 3.6.1.3 0 .7-.2 1z"/></svg>214-555-0148</li>
      <li><svg viewBox="0 0 24 24"><path d="M7 1h10a2 2 0 0 1 2 2v18a2 2 0 0 1-2 2H7a2 2 0 0 1-2-2V3a2 2 0 0 1 2-2zm0 3v14h10V4z"/></svg>480-555-0192</li>
      <li><svg viewBox="0 0 24 24"><path d="M2 5h20v14H2zm2 2v.5l8 5 8-5V7z"/></svg>DWhitcombe@meridianlodging.com</li>
      <li><svg viewBox="0 0 24 24"><circle cx="12" cy="12" r="10"/></svg>MLPOilField.com</li>
    </ul>
  </div>

  <div class="tagline-band">Oil Field Housingon Auropilot</div>
</section>

<section class="card card--back">
  <div class="pitch">
    <h2 class="pitch__heading">Experienced Provider To Oil, Gas,<br>Energy &amp; Construction Industries</h2>
    <ul class="benefits">
      <li><svg viewBox="0 0 24 24" fill="none" stroke="#fff" stroke-width="2.4" stroke-linecap="round"><path d="M20 11.5A8.5 8.5 0 1 1 15 4"/><path d="M8 11l4 4 9-10"/></svg>Consolidated Billing</li>
      <li><svg viewBox="0 0 24 24" fill="none" stroke="#fff" stroke-width="2.4" stroke-linecap="round"><path d="M20 11.5A8.5 8.5 0 1 1 15 4"/><path d="M8 11l4 4 9-10"/></svg>Full Service Corporate Lodging</li>
      <li><svg viewBox="0 0 24 24" fill="none" stroke="#fff" stroke-width="2.4" stroke-linecap="round"><path d="M20 11.5A8.5 8.5 0 1 1 15 4"/><path d="M8 11l4 4 9-10"/></svg>Live Customer Support 24/7/365</li>
      <li><svg viewBox="0 0 24 24" fill="none" stroke="#fff" stroke-width="2.4" stroke-linecap="round"><path d="M20 11.5A8.5 8.5 0 1 1 15 4"/><path d="M8 11l4 4 9-10"/></svg>Proven Track Record&nbsp; Of Performance</li>
      <li><svg viewBox="0 0 24 24" fill="none" stroke="#fff" stroke-width="2.4" stroke-linecap="round"><path d="M20 11.5A8.5 8.5 0 1 1 15 4"/><path d="M8 11l4 4 9-10"/></svg>Best Negotiated Rates &amp; No Additional Fees</li>
    </ul>
  </div>
  <div class="brand-seal">Meridian<br>Lodging<br>Partners</div>
</section>

</body>
</html>
```